BROCHURE VELNORA

I HAVE TO REORGANIZE THE ATTACHED BROCHURE

Target Market(s)

FACTORY USE

Industry/Entity Type

MEDICAL COSMETIC

Font styles to use
Serif

Colors
0054AA
0677BA
7BADD7
CADEEF
E8F1F8

Requirements
Must have
• I need only reorganize the brochure

```html
<!DOCTYPE html>
<html lang="it">
<head>
<meta charset="utf-8">
<title>VELNORA – Brochure</title>
<link href="https://fonts.googleapis.com/css2?family=Comfortaa:wght@400;500;600&family=Quicksand:wght@400;500;600;700&display=swap" rel="stylesheet">
<style>
:root{
  --navy:#0f4c8e;
  --blue:#0054AA;
  --sky:#29a9e1;
  --sky-soft:#7BADD7;
  --pale:#CADEEF;
  --mist:#E8F1F8;
  --grey:#7d7d7d;
  --ink:#222;
  --page:#ffffff;
}
*{box-sizing:border-box;margin:0;padding:0}
html,body{width:1200px;height:634px;overflow:hidden;background:var(--page)}
body{position:relative;font-family:"Quicksand",sans-serif;color:var(--ink)}
.slide{position:absolute;width:376px;height:283px;background:#fff;border:1px solid #d6d6d6;overflow:hidden}
.slide-number{position:absolute;font-size:11px;color:#444;font-family:"Quicksand",sans-serif}
.footer-band{position:absolute;left:0;right:0;bottom:0;height:60px;background:linear-gradient(180deg,rgba(255,255,255,0) 0%,#eceff2 55%,#dfe3e7 100%)}
.footer-mark{position:absolute;left:5px;bottom:4px;font-size:5.5px;color:var(--grey)}
.footer-page{position:absolute;right:6px;bottom:4px;font-size:5.5px;color:var(--grey)}
.brand{position:absolute;right:9px;top:7px;display:flex;align-items:center;gap:3px;font-family:"Quicksand",sans-serif;font-weight:700;font-size:9px;color:var(--blue);letter-spacing:.2px}
.brand::before{content:"";width:7px;height:7px;border-radius:50%;background:var(--sky)}
.title{position:absolute;font-family:"Comfortaa",sans-serif;color:var(--navy);line-height:1.02}
.rule{position:absolute;left:0;height:2px;background:var(--sky)}
.vertical{position:absolute;font-family:"Comfortaa",sans-serif;color:var(--navy);font-size:25px;transform:rotate(-90deg);transform-origin:left top;white-space:nowrap;letter-spacing:.5px}
.lead{position:absolute;font-family:"Quicksand",sans-serif;color:var(--sky);line-height:1.05}
.list{position:absolute;font-size:8.6px;color:var(--grey);line-height:11.4px;text-transform:none}
.photo{position:absolute;border-radius:50%}
</style>
</head>
<body>

<!-- Slide 25 -->
<section class="slide" style="left:5px;top:4px">
  <div class="footer-band"></div>
  <h2 class="title" style="left:40px;top:12px;font-size:15.5px">Ricordiamo che esiste un<br>andamento stagionale della caduta</h2>
  <div class="rule" style="top:48px;width:320px"></div>
  <div class="brand">VELNORA</div>
  <svg style="position:absolute;left:55px;top:55px" width="270" height="153" viewBox="70 70 345 195" font-family="Quicksand, sans-serif">
    <g stroke="#9a9a9a" stroke-width=".7">
      <line x1="84" y1="75" x2="84" y2="253"/><line x1="106" y1="75" x2="106" y2="253"/><line x1="128" y1="75" x2="128" y2="253"/><line x1="151" y1="75" x2="151" y2="253"/><line x1="173" y1="75" x2="173" y2="253"/><line x1="195" y1="75" x2="195" y2="253"/><line x1="217" y1="75" x2="217" y2="253"/><line x1="239" y1="75" x2="239" y2="253"/><line x1="262" y1="75" x2="262" y2="253"/><line x1="284" y1="75" x2="284" y2="253"/><line x1="306" y1="75" x2="306" y2="253"/><line x1="328" y1="75" x2="328" y2="253"/><line x1="350" y1="75" x2="350" y2="253"/>
    </g>
    <line x1="84" y1="75" x2="385" y2="75" stroke="#9a9a9a" stroke-width=".8"/>
    <line x1="84" y1="117" x2="385" y2="117" stroke="#9a9a9a" stroke-width=".8" stroke-dasharray="4 3"/>
    <line x1="84" y1="150" x2="385" y2="150" stroke="#bbb" stroke-width=".7" stroke-dasharray="4 3"/>
    <line x1="84" y1="181" x2="385" y2="181" stroke="#111" stroke-width="1.6" stroke-dasharray="4 3"/>
    <line x1="84" y1="210" x2="385" y2="210" stroke="#bbb" stroke-width=".7" stroke-dasharray="4 3"/>
    <line x1="78" y1="226" x2="385" y2="226" stroke="#111" stroke-width="1"/>
    <line x1="90" y1="182" x2="151" y2="138" stroke="#1d4d86" stroke-width="7"/>
    <line x1="237" y1="181" x2="286" y2="115" stroke="#4bb8e6" stroke-width="7"/>
    <polyline points="84,171 95,182 151,138 208,226 286,115 350,181 358,168" fill="none" stroke="#111" stroke-width="1.8"/>
    <g font-size="8" font-style="italic" font-family="Georgia, serif" fill="#111">
      <text x="390" y="116">2/</text><text x="390" y="125">1000</text>
      <text x="390" y="180">1/</text><text x="390" y="189">1000</text>
      <text x="390" y="222">0,3/</text><text x="390" y="231">1000</text><text x="390" y="240">die</text>
    </g>
    <g font-size="7.5" fill="#222" text-anchor="middle">
      <text x="84" y="261">G</text><text x="106" y="261">F</text><text x="128" y="261">M</text><text x="151" y="261">A</text><text x="173" y="261">M</text><text x="195" y="261">G</text><text x="217" y="261">L</text><text x="239" y="261">A</text><text x="262" y="261">S</text><text x="284" y="261">O</text><text x="306" y="261">N</text><text x="328" y="261">D</text><text x="350" y="261">G</text>
    </g>
  </svg>
  <div style="position:absolute;left:48px;top:223px;width:8px;height:25px;background:#1d4d86"></div>
  <div style="position:absolute;left:61px;top:217px;width:130px">
    <div style="font-size:10px;color:var(--navy);text-decoration:underline;font-weight:500">VASODILATAZIONE</div>
    <div style="font-size:6.6px;color:#444;line-height:8px">I capelli in fase telogen cadono prima perché spinti dai nuovi</div>
  </div>
  <div style="position:absolute;left:197px;top:223px;width:8px;height:25px;background:#4bb8e6"></div>
  <div style="position:absolute;left:211px;top:217px;width:120px">
    <div style="font-size:10px;color:var(--sky);text-decoration:underline;font-weight:500">VASOCOSTRIZIONE</div>
    <div style="font-size:6.6px;color:var(--sky);line-height:8px">I capelli in fase anagen crescono meno. È la fase più delicata</div>
  </div>
  <span class="footer-mark">© VELNORA</span><span class="footer-page">25</span>
</section>
<span class="slide-number" style="left:6px;top:294px">25</span>

<!-- Slide 26 -->
<section class="slide" style="left:411px;top:4px">
  <div class="footer-band"></div>
  <h2 class="title" style="left:41px;top:10px;font-size:17px">In quali casi si parla di<br>evento anomalo?</h2>
  <div class="rule" style="top:50px;width:235px"></div>
  <div class="brand">VELNORA</div>
  <div style="position:absolute;left:16px;top:68px;width:175px">
    <div style="font-size:15px;color:var(--navy);font-weight:500">ALOPECIA:</div>
    <div style="font-size:10.5px;color:var(--sky);line-height:12.5px">È la caduta dei capelli temporanea (AA)<br>o una perdita di capelli precoce e definitiva (CALVIZIE).</div>
    <div style="font-size:15px;color:var(--navy);font-weight:500;margin-top:9px">I SINTOMI:</div>
    <ul style="font-size:9.6px;color:var(--sky);line-height:11.5px;list-style:none">
      <li>• CADUTA DEI CAPELLI ACUTA<br>&nbsp;&nbsp;O CONTINUA</li>
      <li>• SPORADICAMENTE PRURITO<br>&nbsp;&nbsp;ALLA CUTE</li>
      <li>• DOLORE AL CUOIO<br>&nbsp;&nbsp;CAPELLUTO</li>
    </ul>
  </div>
  <div role="img" aria-label="Schema della calvizie, stadio I" style="position:absolute;left:198px;top:69px;width:77px;height:41px;border:1px solid var(--pale);background:linear-gradient(135deg,var(--mist),#c9dcee)"></div>
  <div role="img" aria-label="Schema della calvizie, stadio II" style="position:absolute;left:289px;top:69px;width:78px;height:41px;border:1px solid var(--pale);background:linear-gradient(135deg,var(--mist),#c9dcee)"></div>
  <div role="img" aria-label="Schema della calvizie, stadio III" style="position:absolute;left:198px;top:112px;width:77px;height:41px;border:1px solid var(--pale);background:linear-gradient(135deg,var(--mist),#c9dcee)"></div>
  <div role="img" aria-label="Schema della calvizie, stadio III vertex" style="position:absolute;left:289px;top:112px;width:78px;height:41px;border:1px solid var(--pale);background:linear-gradient(135deg,var(--mist),#c9dcee)"></div>
  <div role="img" aria-label="Schema della calvizie, stadio IV" style="position:absolute;left:198px;top:155px;width:77px;height:41px;border:1px solid var(--pale);background:linear-gradient(135deg,var(--mist),#c9dcee)"></div>
  <div role="img" aria-label="Schema della calvizie, stadio V" style="position:absolute;left:289px;top:155px;width:78px;height:41px;border:1px solid var(--pale);background:linear-gradient(135deg,var(--mist),#c9dcee)"></div>
  <div role="img" aria-label="Schema della calvizie, stadio VI" style="position:absolute;left:198px;top:199px;width:77px;height:41px;border:1px solid var(--pale);background:linear-gradient(135deg,var(--mist),#c9dcee)"></div>
  <div role="img" aria-label="Schema della calvizie, stadio VII" style="position:absolute;left:289px;top:199px;width:78px;height:41px;border:1px solid var(--pale);background:linear-gradient(135deg,var(--mist),#c9dcee)"></div>
  <span class="footer-mark">© VELNORA</span><span class="footer-page">26</span>
</section>
<span class="slide-number" style="left:412px;top:294px">26</span>

<!-- Slide 27 -->
<section class="slide" style="left:816px;top:4px">
  <div class="footer-band"></div>
  <div class="brand">VELNORA</div>
  <div class="vertical" style="left:9px;top:236px">MAPPA PRODOTTI</div>
  <h2 class="lead" style="left:50px;top:38px;font-size:15.5px;font-family:'Comfortaa',sans-serif">INSERIRE IMMAGINE DEI PRODOTTI<br>DETOSSINANTI A DISPOSIZIONE</h2>
  <div class="list" style="left:56px;top:76px">
    <div style="color:#666">INSERIRE I VARI TRATTAMENTI per AGA come da mail:</div>
    <div>CUTIS PURA MASCHERA</div>
    <div>SH CUTIS PURA – EQUILIA – IDRALIA - BIOLENA</div>
    <div>FIALE CUTIS PURA FASE 2</div>
    <div style="margin-top:11px">SHAMPOO IDRALIA</div>
    <div>FIALE POST SH OXYLIA- IDRALIA – AQUALIA</div>
    <div style="margin-top:11px">LOZIONE DERMAVIVA</div>
    <div>SH CUTIS PURA – BIOLENA – EQUILIA ETC.</div>
    <div>FIALE POST SH NUTRIVA</div>
    <div>CAPIL COMPLEX</div>
    <div>LOZIONE UOMO NOTTE – FORTIVEL</div>
  </div>
  <span class="footer-mark">© VELNORA</span><span class="footer-page">27</span>
</section>
<span class="slide-number" style="left:817px;top:294px">27</span>

<!-- Slide 28 -->
<section class="slide" style="left:5px;top:328px">
  <div class="footer-band"></div>
  <h2 class="title" style="left:41px;top:27px;font-size:18.5px">ALOPECIA AREATA</h2>
  <div class="rule" style="top:46px;width:235px"></div>
  <div class="brand">VELNORA</div>
  <p class="lead" style="left:0;width:370px;top:70px;font-size:14.5px;text-align:center;line-height:17.5px">Forma benigna ma recidivante;<br>Chiazze rotondeggianti di<br>perdita localizzata.</p>
  <div class="photo" role="img" aria-label="Foto di una chiazza di alopecia areata sulla nuca" style="left:42px;top:122px;width:140px;height:98px;background:radial-gradient(ellipse at 55% 45%,#b79277 0%,#5a3a2a 55%,#2a1a14 100%)"></div>
  <div class="photo" role="img" aria-label="Foto di una chiazza di alopecia areata tra capelli grigi" style="left:198px;top:120px;width:147px;height:99px;background:radial-gradient(ellipse at 50% 40%,#cdbcbb 0%,#8f8784 50%,#5d5754 100%)"></div>
  <span class="footer-mark">© VELNORA</span><span class="footer-page">28</span>
</section>
<span class="slide-number" style="left:6px;top:618px">28</span>

<!-- Slide 29 -->
<section class="slide" style="left:411px;top:328px">
  <div class="footer-band"></div>
  <div class="brand">VELNORA</div>
  <div class="vertical" style="left:9px;top:236px">MAPPA PRODOTTI</div>
  <h2 class="lead" style="left:118px;top:101px;font-size:15.5px;font-family:'Comfortaa',sans-serif">INSERIRE I VARI<br>TRATTAMENTI per AA :</h2>
  <div class="list" style="left:119px;top:139px">
    <div>LOZIONE POLIVALENTE TEA TREE</div>
    <div>SH BIOLENA</div>
  </div>
  <span class="footer-mark">© VELNORA</span><span class="footer-page">29</span>
</section>
<span class="slide-number" style="left:412px;top:618px">29</span>

<!-- Slide 30 -->
<section class="slide" style="left:816px;top:328px">
  <div class="footer-band"></div>
  <div class="brand">VELNORA</div>
  <h2 class="title" style="left:41px;top:25px;font-size:17.5px;line-height:22px">IEC, Calvizie da Carenze/eccesso,<br>ALOPECIE CICATRIZIALI</h2>
  <div class="rule" style="top:72px;width:191px"></div>
  <p style="position:absolute;left:0;width:376px;top:90px;text-align:center;font-size:12px;line-height:15.5px;color:#777">
    <span style="color:var(--sky)">Ipotrichie diffuse e Calvizie.</span><br>
    Oggi si conoscono differenti forme di calvizie<br>
    nell'uomo e nella donna. <span style="color:var(--sky)">Molto spesso<br>vengono non correttamente identificate e<br>quindi trattate in modo sbagliato.</span>
  </p>
  <div class="photo" role="img" aria-label="Foto di diradamento diffuso su capelli ramati" style="left:60px;top:189px;width:133px;height:78px;background:radial-gradient(ellipse at 50% 45%,#e9b58f 0%,#b8653a 55%,#7a3a1c 100%)"></div>
  <div class="photo" role="img" aria-label="Foto di diradamento della riga su capelli scuri" style="left:207px;top:181px;width:110px;height:86px;background:radial-gradient(ellipse at 50% 45%,#8a8a8a 0%,#3b3b3b 55%,#1c1c1c 100%)"></div>
  <span class="footer-mark">© VELNORA</span><span class="footer-page">30</span>
</section>
<span class="slide-number" style="left:817px;top:618px">30</span>

</body>
</html>
```